Spiritual Healing bussiness needs logo/business card

Simple, clean looking logo/card
For spiritual business with healing services and occult rituals

Contact Information for Business Card

Needs my name: Corwin Halley
Business name: Veyra Healing Shop
Services provided and worded in this way:

Reiki Healing
Tarot
Oils
Rituals Of Change

Can look occult like but with light energy.

Colors
0255a3
3276b5
85abd2
33a6d7
85cae6
0292cd

```html
<!DOCTYPE html>
<html lang="en">
<head>
<meta charset="utf-8">
<title>Veyra Healing Shop – Business Cards</title>
<link href="https://fonts.googleapis.com/css2?family=Cormorant+Garamond:ital,wght@1,600;1,700&display=swap" rel="stylesheet">
<style>
  :root {
    --page-bg: #e9e7ee;
    --violet-deep: #4a3a7c;
    --violet: #8a5fae;
    --lavender: #c8b6e0;
    --mist: #f1eef6;
    --ink: #1d1324;
    --frame-blue: #85abd2;
    --frame-blue-deep: #3276b5;
    --glow: rgba(255, 255, 255, 0.55);
  }
  * { box-sizing: border-box; margin: 0; padding: 0; }
  html, body {
    width: 1200px;
    height: 900px;
    overflow: hidden;
    background: var(--page-bg);
  }
  .sheet {
    width: 1200px;
    height: 900px;
    display: flex;
    flex-direction: column;
    align-items: center;
    justify-content: center;
    gap: 40px;
  }
  .card {
    position: relative;
    width: 700px;
    height: 400px;
    border-radius: 4px;
    overflow: hidden;
    box-shadow: 0 6px 18px rgba(40, 20, 60, 0.18);
    background:
      radial-gradient(ellipse at 18% 10%, rgba(190, 130, 90, 0.35) 0%, transparent 35%),
      linear-gradient(135deg, var(--violet-deep) 0%, var(--violet) 28%, var(--lavender) 58%, var(--mist) 82%, #ffffff 100%);
    font-family: "Cormorant Garamond", "Times New Roman", serif;
    font-style: italic;
    color: var(--ink);
  }
  .card__energy-art {
    position: absolute;
    left: 170px;
    top: 40px;
    width: 300px;
    height: 320px;
    border-radius: 50%;
    background: radial-gradient(ellipse at 50% 40%, var(--glow) 0%, rgba(150, 100, 190, 0.45) 35%, rgba(150, 100, 190, 0) 70%);
  }
  .card__frame {
    position: absolute;
    inset: 22px;
    border: 4px solid var(--frame-blue);
    border-image: linear-gradient(135deg, var(--frame-blue-deep), var(--frame-blue)) 1;
  }

  /* Front */
  .card--front .card__energy-art { left: 120px; }
  .brand-block {
    position: absolute;
    right: 60px;
    top: 70px;
    text-align: right;
  }
  .brand-block__shop {
    font-size: 46px;
    font-weight: 600;
    letter-spacing: 0.5px;
  }
  .brand-block__owner {
    margin-top: 4px;
    margin-right: 30px;
    font-size: 34px;
    font-weight: 600;
  }

  /* Back */
  .service-list {
    position: absolute;
    left: 190px;
    top: 70px;
    list-style: none;
    font-size: 42px;
    font-weight: 700;
    line-height: 1.05;
  }
  .service-list__item:nth-child(1) { padding-left: 40px; }
  .service-list__item:nth-child(2) { padding-left: 26px; }
  .service-list__item:nth-child(3) { padding-left: 14px; }
</style>
</head>
<body>
<main class="sheet">
  <section class="card card--front" aria-label="Business card front">
    <div class="card__energy-art" role="img" aria-label="Meditating figure surrounded by radiant energy lines"></div>
    <div class="brand-block">
      <h1 class="brand-block__shop">Veyra Healing Shop</h1>
      <p class="brand-block__owner">Corwin Halley</p>
    </div>
  </section>

  <section class="card card--back" aria-label="Business card back">
    <div class="card__energy-art" role="img" aria-label="Meditating figure surrounded by radiant energy lines"></div>
    <div class="card__frame"></div>
    <ul class="service-list">
      <li class="service-list__item">Reiki Healing</li>
      <li class="service-list__item">Tarot</li>
      <li class="service-list__item">Oils</li>
      <li class="service-list__item">Rituals Of Change</li>
    </ul>
  </section>
</main>
</body>
</html>
```